Business Card Project

We are a small consulting firm. You can experiment with any design.
Must have:
1) Company name - OLUNDEX International
2) Company slogan - simple solutions for complex problems
3) Name/Title/Phone/Email/WWW/ - use anything you like as an example.

Industry/Entity Type

Business

```html
<!DOCTYPE html>
<html lang="en">
<head>
<meta charset="utf-8">
<title>OLUNDEX International – Business Card</title>
<link rel="stylesheet" href="https://fonts.googleapis.com/css2?family=Open+Sans:wght@400;700&display=swap">
<style>
  :root {
    --backdrop: #1f1f1f;
    --sky-light: #b9e3f7;
    --sky: #5cc3ee;
    --sky-deep: #12a3e2;
    --navy: #1a6db5;
    --paper: #f2f3f5;
    --ink: #5a5a5a;
    --ink-soft: #6c6c6c;
    --white: #ffffff;
  }
  * { margin: 0; padding: 0; box-sizing: border-box; }
  html, body {
    width: 1200px; height: 900px; overflow: hidden;
    background: var(--backdrop);
    font-family: "Open Sans", Arial, sans-serif;
  }
  .stage {
    width: 1200px; height: 900px;
    display: flex; flex-direction: column;
    align-items: center; justify-content: center; gap: 56px;
  }
  .card {
    position: relative;
    width: 560px; height: 320px;
    overflow: hidden;
  }

  /* Front side */
  .card--front {
    background:
      radial-gradient(circle at 115% 10%, rgba(255,255,255,0.10) 0 38%, transparent 38.2%),
      radial-gradient(circle at 115% 10%, rgba(255,255,255,0.08) 0 55%, transparent 55.2%),
      radial-gradient(circle at 115% 10%, rgba(255,255,255,0.06) 0 72%, transparent 72.2%),
      linear-gradient(100deg, var(--sky-light) 0%, var(--sky) 45%, var(--sky-deep) 100%);
  }
  .wordmark {
    position: absolute;
    display: flex; align-items: center; gap: 14px;
  }
  .wordmark__dot {
    width: 34px; height: 34px; border-radius: 50%;
    background: var(--navy);
  }
  .wordmark__name {
    font-weight: 400; color: var(--ink);
    letter-spacing: 0.04em; white-space: nowrap;
  }
  .card--front .wordmark { left: 70px; top: 118px; }
  .card--front .wordmark__name { font-size: 34px; }
  .front-url {
    position: absolute; left: 300px; top: 180px;
    font-size: 12px; color: var(--white); letter-spacing: 0.02em;
  }
  .slogan {
    position: absolute; left: 118px; top: 214px;
    font-size: 14px; color: var(--white); letter-spacing: 0.03em;
  }

  /* Contact side */
  .card--contact { background: var(--paper); }
  .card--contact .swoosh { position: absolute; inset: 0; }
  .card--contact .wordmark { left: 50px; top: 58px; }
  .card--contact .wordmark__dot { width: 28px; height: 28px; }
  .card--contact .wordmark__name { font-size: 27px; }
  .holder {
    position: absolute; left: 40px; top: 238px;
    color: var(--ink);
  }
  .holder__name { font-size: 22px; font-weight: 700; line-height: 1.05; letter-spacing: 0.01em; }
  .holder__title { font-size: 14px; color: var(--ink-soft); }
  .contact-list {
    position: absolute; left: 304px; top: 176px;
    list-style: none; font-size: 13px; color: var(--ink);
  }
  .contact-list li {
    display: flex; align-items: center; gap: 8px; height: 22px;
  }
  .contact-list svg { width: 13px; height: 13px; fill: var(--ink); flex: none; }
</style>
</head>
<body>
<main class="stage">

  <section class="card card--front" aria-label="Business card front">
    <div class="wordmark">
      <span class="wordmark__dot"></span>
      <span class="wordmark__name">OLUNDEX International</span>
    </div>
    <p class="front-url">www.OlundexInternational.com</p>
    <p class="slogan">simple solutions for complex problems</p>
  </section>

  <section class="card card--contact" aria-label="Business card contact side">
    <svg class="swoosh" viewBox="0 0 560 320" preserveAspectRatio="none" aria-hidden="true">
      <defs>
        <linearGradient id="band" x1="0" y1="0" x2="1" y2="0">
          <stop offset="0" stop-color="#2fb2ea"/>
          <stop offset="1" stop-color="#8fd2f2"/>
        </linearGradient>
      </defs>
      <path d="M0 176 Q 260 150 560 88 L560 320 L0 320 Z" fill="url(#band)"/>
      <path d="M0 170 Q 250 140 470 100" fill="none" stroke="#1a6db5" stroke-width="5"/>
      <path d="M0 178 Q 260 152 560 96" fill="none" stroke="#ffffff" stroke-width="3"/>
    </svg>

    <div class="wordmark">
      <span class="wordmark__dot"></span>
      <span class="wordmark__name">OLUNDEX International</span>
    </div>

    <ul class="contact-list">
      <li>
        <svg viewBox="0 0 16 16"><path d="M3 1h4l1 4-2 1.5a9 9 0 0 0 3.5 3.5L11 8l4 1v4a2 2 0 0 1-2 2A12 12 0 0 1 1 3a2 2 0 0 1 2-2z"/></svg>
        + 1 (1) 555 014 2290
      </li>
      <li>
        <svg viewBox="0 0 16 16"><path d="M1 3h14v10H1zM2 4.2v.6l6 4 6-4v-.6l-6 4z" fill-rule="evenodd"/></svg>
        marisa@OlundexInternational.com
      </li>
      <li>
        <svg viewBox="0 0 16 16"><path d="M8 1a7 7 0 1 0 0 14A7 7 0 0 0 8 1zm0 1.5a5.5 5.5 0 0 1 0 11 2 5.5 0 0 1 0-11zM3 7.3h10v1.4H3z"/></svg>
        www.OlundexInternational.com
      </li>
    </ul>

    <div class="holder">
      <p class="holder__name">MARISA VALE</p>
      <p class="holder__title">Managing Director</p>
    </div>
  </section>

</main>
</body>
</html>
```